Business card for law firm

Need business card for new law firm. Think confident, authoritative, conservative, but not stuffy or old-fashioned.

Contact Information for Business Card

Content for card - logo (uploaded), plus the following:

Paul Wexbury (larger font)
Managing Partner (larger font, but not as large as name)
Level 9, 41 Tansy Lane
Sydney NSW 2000
Main Tel 02 7346 2190
Direct Tel 02 6273 4415
Email paul@qvlegal.com.au
www.qvlegal.com.au

Letterhead design should include logo plus:
Level 9, 41 Tansy Lane
Sydney NSW 2000
Tel 02 6273 4415
www.qvlegal.com.au

```html
<!DOCTYPE html>
<html lang="en">
<head>
<meta charset="utf-8">
<title>Quayvale Lawyers – Business Card</title>
<link rel="stylesheet" href="https://fonts.googleapis.com/css2?family=Ubuntu:wght@400;500&family=Roboto:wght@400&display=swap">
<style>
  :root {
    --paper: #ffffff;
    --navy: #030b6c;
    --ink: #111111;
    --white: #ffffff;
    --title-grey: #c7d0df;
    --rule: #6f7bb0;
  }
  html, body {
    margin: 0;
    padding: 0;
    overflow: hidden;
    background: var(--paper);
  }
  .card {
    position: relative;
    width: 1200px;
    height: 686px;
    background: var(--paper);
    overflow: hidden;
  }
  .brand {
    position: absolute;
    left: 0;
    top: 0;
    width: 1200px;
    height: 465px;
    display: flex;
    align-items: center;
    justify-content: center;
    gap: 28px;
  }
  .brand__square {
    width: 64px;
    height: 64px;
    background: var(--navy);
    flex: none;
  }
  .brand__name {
    margin: 0;
    font-family: "Ubuntu", "Helvetica", sans-serif;
    font-weight: 500;
    font-size: 60px;
    line-height: 1;
    color: var(--ink);
  }
  .contact-band {
    position: absolute;
    left: 0;
    top: 465px;
    width: 1200px;
    height: 221px;
    background: var(--navy);
  }
  .person {
    position: absolute;
    right: 620px;
    top: 70px;
    text-align: right;
  }
  .person__name {
    margin: 0;
    font-family: "Ubuntu", "Helvetica", sans-serif;
    font-weight: 500;
    font-size: 44px;
    line-height: 1;
    color: var(--white);
    text-shadow: 1px 2px 3px rgba(0, 0, 0, 0.45);
    letter-spacing: 0.5px;
  }
  .person__title {
    margin: 4px 0 0;
    font-family: "Ubuntu", "Helvetica", sans-serif;
    font-weight: 400;
    font-size: 27px;
    line-height: 1;
    color: var(--title-grey);
    text-shadow: 1px 1px 2px rgba(0, 0, 0, 0.35);
  }
  .divider {
    position: absolute;
    left: 632px;
    top: 16px;
    width: 2px;
    height: 188px;
    background: var(--rule);
  }
  .contact-list {
    position: absolute;
    left: 680px;
    top: 24px;
    margin: 0;
    padding: 0;
    list-style: none;
    font-family: "Roboto", "Arial", sans-serif;
    font-size: 19px;
    line-height: 24px;
    color: var(--white);
  }
  .contact-item {
    display: flex;
    align-items: center;
    margin-bottom: 8px;
  }
  .contact-item--email { margin-bottom: 3px; }
  .contact-icon {
    width: 22px;
    height: 22px;
    margin-right: 34px;
    flex: none;
  }
</style>
</head>
<body>
<div class="card">
  <header class="brand">
    <div class="brand__square"></div>
    <p class="brand__name">Quayvale Lawyers</p>
  </header>

  <section class="contact-band">
    <div class="person">
      <h1 class="person__name">Paul Wexbury</h1>
      <p class="person__title">Managing Partner</p>
    </div>

    <div class="divider"></div>

    <ul class="contact-list">
      <li class="contact-item">
        <svg class="contact-icon" viewBox="0 0 24 24" aria-hidden="true">
          <path d="M12 2a7 7 0 0 0-7 7c0 5 7 13 7 13s7-8 7-13a7 7 0 0 0-7-7z" fill="#fff"/>
          <circle cx="12" cy="9" r="2.6" fill="#030b6c"/>
        </svg>
        <span>Level 9, 41 Tansy Lane<br>Sydney NSW 2000</span>
      </li>
      <li class="contact-item">
        <svg class="contact-icon" viewBox="0 0 24 24" aria-hidden="true">
          <rect x="6" y="2" width="12" height="20" rx="2" fill="#fff"/>
          <rect x="8" y="5" width="8" height="12" fill="#030b6c"/>
          <circle cx="12" cy="19.3" r="1" fill="#030b6c"/>
        </svg>
        <span>02 7346 2190<br>02 6273 4415</span>
      </li>
      <li class="contact-item contact-item--email">
        <svg class="contact-icon" viewBox="0 0 24 24" aria-hidden="true">
          <path d="M2 10l10-7 10 7v11H2z" fill="#fff"/>
          <path d="M2 10l10 7 10-7" fill="none" stroke="#030b6c" stroke-width="1.6"/>
          <rect x="6" y="6" width="12" height="6" fill="#fff"/>
          <path d="M8 8h8M8 10.5h6" stroke="#030b6c" stroke-width="1"/>
        </svg>
        <span>paul@qvlegal.com.au</span>
      </li>
      <li class="contact-item">
        <svg class="contact-icon" viewBox="0 0 24 24" aria-hidden="true">
          <g fill="none" stroke="#fff" stroke-width="1.6">
            <circle cx="12" cy="12" r="9"/>
            <ellipse cx="12" cy="12" rx="4" ry="9"/>
            <path d="M3 12h18M4.5 7.5h15M4.5 16.5h15"/>
          </g>
        </svg>
        <span>www.qvlegal.com.au</span>
      </li>
    </ul>
  </section>
</div>
</body>
</html>
```